Land Buying Company Needs Letterhead for Direct Mail Marketing to Land Owners

We are looking for a professional letterhead that we will be including in our direct mail marketing. We will be sending this to land owners who may be interested in selling or purchasing land.

The letterhead needs to be editable. Headers and footers would look nice, but we are open. We would want it to include our address, website, phone, and email info. For right now the address to use for design purposes would the following:

Address: 415 Bramwell Avenue #600
Dallas, TX 75219
Website - www.quillridgeacres.example
Email - info@quillridgeacres.example
Phone - 866-402-ACRE

I have attached our logo zip file that we just had done on Pixel Guild. Let me know what questions you have, and thank you.

```html
<!DOCTYPE html>
<html lang="en">
<head>
<meta charset="utf-8">
<title>Quill Ridge Acres Letterhead</title>
<link rel="stylesheet" href="https://fonts.googleapis.com/css2?family=Montserrat:wght@600&family=Open+Sans:wght@400;600&display=swap">
<style>
  :root {
    --backdrop: #dccdb4;
    --paper: #ffffff;
    --forest: #3f5a1d;
    --lime: #8cc63f;
    --sage: #d3e4b4;
    --ink: #333333;
  }
  html, body {
    margin: 0;
    width: 1200px;
    height: 898px;
    overflow: hidden;
    background: var(--backdrop);
  }
  .letterhead {
    position: absolute;
    left: 290px;
    top: 49px;
    width: 620px;
    height: 800px;
    background: var(--paper);
    overflow: hidden;
    font-family: "Open Sans", Arial, sans-serif;
    color: var(--ink);
  }
  .bands {
    position: absolute;
    inset: 0;
  }
  .brand {
    position: absolute;
    top: 22px;
    right: 42px;
    display: flex;
    align-items: center;
    gap: 10px;
  }
  .brand-mark {
    width: 30px;
    height: 30px;
    border-radius: 50%;
    background: var(--paper);
  }
  .brand-name {
    font-family: "Montserrat", Arial, sans-serif;
    font-weight: 600;
    font-size: 17px;
    letter-spacing: 1.5px;
    color: var(--lime);
    text-transform: uppercase;
  }
  .letter {
    position: absolute;
    top: 150px;
    left: 62px;
    width: 470px;
    font-size: 9.5px;
    line-height: 1.55;
  }
  .letter p { margin: 0 0 14px; }
  .letter .recipient { margin-bottom: 22px; }
  .letter .signoff { margin-top: 40px; }
  .contact {
    position: absolute;
    left: 290px;
    bottom: 48px;
    display: grid;
    grid-template-columns: auto auto;
    gap: 8px 14px;
    font-size: 8px;
    font-weight: 600;
    color: var(--paper);
  }
  .contact-item {
    display: flex;
    align-items: center;
    gap: 5px;
  }
  .contact-item svg { width: 11px; height: 11px; flex: none; }
</style>
</head>
<body>
  <main class="letterhead">
    <svg class="bands" width="620" height="800" viewBox="0 0 620 800" aria-hidden="true">
      <!-- header -->
      <rect x="0" y="0" width="620" height="118" fill="var(--forest)"/>
      <rect x="270" y="70" width="350" height="6" fill="var(--lime)"/>
      <rect x="0" y="30" width="190" height="6" fill="var(--lime)"/>
      <rect x="0" y="112" width="620" height="6" fill="var(--lime)"/>
      <!-- faint decorative disc -->
      <circle cx="535" cy="640" r="92" fill="var(--sage)"/>
      <!-- footer -->
      <rect x="330" y="668" width="290" height="132" fill="var(--forest)"/>
      <rect x="0" y="700" width="620" height="100" fill="var(--forest)"/>
      <rect x="0" y="694" width="330" height="6" fill="var(--lime)"/>
    </svg>

    <div class="brand">
      <span class="brand-mark"></span>
      <span class="brand-name">Quill Ridge Acres</span>
    </div>

    <article class="letter">
      <p>August 14th, 2020</p>
      <p class="recipient">First Last Name<br>Street Address<br>City, State 00000</p>
      <p>Dear Customer,</p>
      <p>Lorem ipsum dolor sit amet, consectetur adipiscing elit. Aenean ut ipsum eget massa hendrerit vestibulum vel in velit. Donec pretium neque velit.</p>
      <p>Aliquam porta lectus nec mauris ornare venenatis. Vivamus non est turpis, et cursus sem. Mauris vehicula erat in diam auctor at bibendum nisl lacinia.</p>
      <p>Morbi imperdiet neque vehicula nunc convallis gravida. Vestibulum iaculis pretium placerat. Integer consequat, est sit amet facilisis eleifend, nibh nibh varius orci, eget dapibus arcu dui non purus. Pellentesque in magna mauris. Duis enim sapien, dictum vitae condimentum a, pulvinar vel lacus. Mauris et molestie nibh. Vestibulum vitae nulla at metus elementum porta sit amet interdum elit. Nulla sollicitudin neque eu nulla volutpat congue.</p>
      <p>Etiam pellentesque, velit id dapibus fermentum, turpis sapien ornare dui, ac tincidunt ligula odio congue purus. Nunc sed ante dui, in porta lectus. Cras nec sem lorem. In hac habitasse platea dictumst. Maecenas id diam quis dui porta tristique. Sed id egestas felis. Donec ullamcorper mattis posuere. Phasellus fermentum eleifend tortor vel dapibus. Vestibulum ante ipsum.</p>
      <p class="signoff">Your Sincerely,<br>Managing Director</p>
    </article>

    <footer class="contact">
      <span class="contact-item">
        <svg viewBox="0 0 12 12" aria-hidden="true"><circle cx="6" cy="6" r="6" fill="var(--lime)"/><path d="M6 2.6a2 2 0 0 0-2 2c0 1.6 2 4.2 2 4.2s2-2.6 2-4.2a2 2 0 0 0-2-2z" fill="var(--forest)"/></svg>
        415 Bramwell Avenue #600 Dallas, TX 75219
      </span>
      <span class="contact-item">
        <svg viewBox="0 0 12 12" aria-hidden="true"><circle cx="6" cy="6" r="6" fill="var(--lime)"/><path d="M4.2 3h1.2l.6 1.5-.8.6a4 4 0 0 0 1.7 1.7l.6-.8 1.5.6v1.2c0 .4-.3.6-.7.6A5 5 0 0 1 3.6 3.7c0-.4.2-.7.6-.7z" fill="var(--forest)"/></svg>
        866-402-ACRE
      </span>
      <span class="contact-item">
        <svg viewBox="0 0 12 12" aria-hidden="true"><circle cx="6" cy="6" r="6" fill="var(--lime)"/><rect x="3" y="4" width="6" height="4.2" fill="var(--forest)"/><path d="M3 4l3 2.3L9 4" stroke="var(--lime)" stroke-width=".7" fill="none"/></svg>
        info@quillridgeacres.example
      </span>
      <span class="contact-item">
        <svg viewBox="0 0 12 12" aria-hidden="true"><circle cx="6" cy="6" r="6" fill="var(--lime)"/><circle cx="6" cy="6" r="3" stroke="var(--forest)" stroke-width=".8" fill="none"/><path d="M3 6h6M6 3c-1.4 1.6-1.4 4.4 0 6M6 3c1.4 1.6 1.4 4.4 0 6" stroke="var(--forest)" stroke-width=".6" fill="none"/></svg>
        www.quillridgeacres.example
      </span>
    </footer>
  </main>
</body>
</html>
```